VELINTA Promotions - Business Card Design Project

We are looking for a classy business cards for Promotion Company based in Toronto, Canada named Velinta Promotions.

Velinta Promotions has an idea and vision to set high standard, be EXCLUSIVE and attract a group of people that will follow us through events we promote (night clubs, brand promotions, music events, and sport events)

We want to present a high standards and classy image to the others...
Updates

Target Market(s)

male/female age 25-40 Target: business owners young entrepreneur - clubing industry - media industry - promotion industry - marketing media industry

Industry/Entity Type

Events

Requirements
Must have
• business cards should be classy, make people feel exclusive , make people react ..

```html
<!DOCTYPE html>
<html lang="en">
<head>
<meta charset="utf-8">
<title>Velinta Promotions – Business Card</title>
<link href="https://fonts.googleapis.com/css2?family=Cinzel:wght@500&family=Tinos:ital,wght@0,400;1,700&display=swap" rel="stylesheet">
<style>
  :root {
    --page: #ffffff;
    --card-top: #0e5288;
    --card-bottom: #072c4b;
    --band: #0f6b9c;
    --brand: #22b9ec;
    --text: #e8f2fa;
    --ink: #111111;
    --flourish: rgba(40, 120, 175, 0.18);
  }
  * { margin: 0; padding: 0; box-sizing: border-box; }
  html, body {
    width: 1200px; height: 900px; overflow: hidden;
    background: var(--page);
    font-family: "Tinos", "Times New Roman", serif;
  }
  .card {
    position: absolute; left: 283px; width: 635px; height: 394px;
    background: linear-gradient(170deg, var(--card-top) 0%, var(--card-bottom) 100%);
    overflow: hidden; color: var(--text);
  }
  .card--front { top: 31px; }
  .card--back { top: 466px; }
  .card__band { position: absolute; inset: 0; width: 635px; height: 394px; }
  .card__flourish {
    position: absolute; right: 0; top: 0; width: 220px; height: 394px;
    background: radial-gradient(ellipse at 70% 40%, var(--flourish), transparent 70%);
  }
  .card__flourish--low {
    left: 40px; right: auto; top: 250px; width: 260px; height: 144px;
    background: radial-gradient(ellipse at 50% 50%, var(--flourish), transparent 70%);
  }
  .brand { position: absolute; color: var(--brand); font-family: "Cinzel", "Times New Roman", serif; font-weight: 500; }
  .brand__name { display: block; line-height: 1; }
  .brand__tag { display: block; text-align: right; letter-spacing: 0.42em; line-height: 1; }
  .card--front .brand { left: 48px; top: 72px; }
  .card--front .brand__name { font-size: 62px; letter-spacing: 0.03em; }
  .card--front .brand__tag { font-size: 14px; margin-top: 6px; margin-right: -4px; }
  .card--back .brand { left: 70px; top: 158px; }
  .card--back .brand__name { font-size: 76px; letter-spacing: 0.03em; }
  .card--back .brand__tag { font-size: 17px; margin-top: 6px; margin-right: -6px; }
  .website { position: absolute; font-size: 17px; color: var(--text); transform: translateX(-50%); white-space: nowrap; }
  .card--front .website { left: 242px; top: 156px; }
  .card--back .website { left: 337px; top: 327px; font-size: 18px; }
  .person { position: absolute; right: 308px; top: 219px; text-align: right; }
  .person__name { font-size: 21px; }
  .person__role { font-size: 13px; font-weight: 700; font-style: italic; margin-top: 6px; }
  .divider { position: absolute; left: 367px; top: 214px; width: 1.5px; height: 86px; background: var(--text); }
  .contacts { position: absolute; left: 396px; top: 223px; list-style: none; font-size: 13.5px; }
  .contacts li { display: flex; align-items: center; height: 25px; }
  .contacts svg { width: 13px; height: 13px; margin-right: 8px; fill: var(--text); }
  .label { position: absolute; font-size: 16px; font-weight: 700; font-style: italic; color: var(--ink); }
  .label--front { left: 957px; top: 426px; }
  .label--back { left: 951px; top: 846px; }
</style>
</head>
<body>

<section class="card card--front">
  <svg class="card__band" viewBox="0 0 635 394" aria-hidden="true">
    <path d="M0 382 Q320 360 635 328 L635 394 L0 394 Z" fill="var(--band)" opacity="0.85"/>
  </svg>
  <div class="card__flourish" role="img" aria-label="Faint floral flourish decoration"></div>
  <div class="card__flourish card__flourish--low" role="img" aria-label="Faint floral flourish decoration"></div>
  <div class="brand">
    <span class="brand__name">VELINTA</span>
    <span class="brand__tag">PROMOTIONS</span>
  </div>
  <p class="website">www.velintapromotions.com</p>
  <div class="person">
    <p class="person__name">Marco Delane</p>
    <p class="person__role">DIRECTOR MANAGER</p>
  </div>
  <div class="divider"></div>
  <ul class="contacts">
    <li><svg viewBox="0 0 16 16"><path d="M5 1h6a1 1 0 0 1 1 1v12a1 1 0 0 1-1 1H5a1 1 0 0 1-1-1V2a1 1 0 0 1 1-1zm0 2v9h6V3z"/></svg>+1 647 555 0193</li>
    <li><svg viewBox="0 0 16 16"><path d="M3.5 1 6 4 4.6 5.8a9 9 0 0 0 5.6 5.6L12 10l3 2.5-1.6 2.3C7 14.5 1.5 9 1.2 2.6z"/></svg>(416) 555 - 0142</li>
    <li><svg viewBox="0 0 16 16"><path d="M1 4h14v9H1z M1.5 4.5 8 9l6.5-4.5" stroke="#0a3a60" stroke-width="1"/></svg>marco@velinta.com</li>
  </ul>
</section>
<p class="label label--front">Front Side</p>

<section class="card card--back">
  <svg class="card__band" viewBox="0 0 635 394" aria-hidden="true">
    <path d="M0 0 L635 0 L635 14 Q300 30 0 110 Z" fill="var(--band)" opacity="0.85"/>
  </svg>
  <div class="card__flourish" role="img" aria-label="Faint floral flourish decoration"></div>
  <div class="card__flourish card__flourish--low" role="img" aria-label="Faint floral flourish decoration"></div>
  <div class="brand">
    <span class="brand__name">VELINTA</span>
    <span class="brand__tag">PROMOTIONS</span>
  </div>
  <p class="website">www.velintapromotions.com</p>
</section>
<p class="label label--back">Back Side</p>

</body>
</html>
```